Tide 4 Tide letterhead design and business card design for electrical company

I need a letterhead that can be used for my invoices and quote books along with emails sent to clients. I have a logo and the logo of Guild tradespeople I just need all my information placed nicely with a good flow.

Business Name: Tide 4 Tide Electrical
Name: Darren Kolvetis
Abn: 57804219362
Licence Number: 39417
Number: 0400683541

Thank you in advanced

Target Market(s)

Electrical Clients

Industry/Entity Type

Business

Contact Information for Business Card

Name: Darren Kolvetis
Abn: 57804219362
Licence Number: 39417
Number: 0400683541

Font styles to use
Sans Serif

Colors

Designer to choose colors to be used in the design.

Requirements
Must have
• Must have my logo, guild tradespeople logo even if its smaller and in the corner and all details
Nice to have
• Domestic Commercial Industrial stated on there somewhere

```html
<!DOCTYPE html>
<html lang="en">
<head>
<meta charset="utf-8">
<title>Tide 4 Tide Electrical – Stationery</title>
<link href="https://fonts.googleapis.com/css2?family=Montserrat:wght@400;600;700&family=Roboto+Condensed:wght@700&display=swap" rel="stylesheet">
<style>
  :root{
    --bg:#e9e9eb;
    --paper:#ffffff;
    --brand-blue:#1d4fa3;
    --brand-deep:#163d82;
    --accent-green:#8cc63f;
    --badge-green:#1f3d2a;
    --ink:#333a45;
    --muted:#7a808a;
  }
  *{box-sizing:border-box;margin:0;padding:0}
  html,body{width:1200px;height:798px;overflow:hidden;background:var(--bg);font-family:"Montserrat",sans-serif;color:var(--ink)}
  .stage{position:relative;width:1200px;height:798px}
  .sheet{position:absolute;background:var(--paper);box-shadow:0 4px 14px rgba(0,0,0,.12);overflow:hidden}

  .brand{position:absolute;display:flex;align-items:center;gap:8px}
  .brand-lead{height:4px;background:var(--brand-blue)}
  .brand-dot{width:10px;height:10px;border-radius:50%;background:var(--brand-blue)}
  .brand-name{font-weight:700;color:var(--brand-blue);white-space:nowrap}
  .owner-name{position:absolute;font-family:"Roboto Condensed",sans-serif;font-weight:700;color:var(--brand-blue);white-space:nowrap}
  .member-badge{position:absolute;display:flex;align-items:center}
  .badge-square{background:var(--badge-green);border-radius:3px}
  .badge-rule{height:4px;background:var(--accent-green)}

  .footer{position:absolute;left:0;right:0;bottom:0;height:24px}
  .footer-band{position:absolute;bottom:0;background:var(--brand-blue);color:#fff;font-weight:600;display:flex;align-items:center;white-space:nowrap}
  .footer-band.left{left:0;justify-content:flex-start}
  .footer-band.right{right:0;justify-content:flex-end}
  .footer-line{position:absolute;bottom:0;left:0;right:0;height:3px;background:var(--brand-deep)}
  .footer-contacts{position:absolute;display:flex;justify-content:center;color:var(--ink);white-space:nowrap}

  /* letterhead */
  .letterhead{left:40px;top:40px;width:380px;height:537px}
  .letterhead .brand{left:0;top:28px}
  .letterhead .brand-lead{width:34px}
  .letterhead .brand-name{font-size:17px}
  .letterhead .owner-name{left:64px;top:54px;font-size:11px}
  .letterhead .member-badge{right:0;top:110px}
  .letterhead .badge-square{width:22px;height:22px}
  .letterhead .badge-rule{width:40px;margin-left:8px}
  .letterhead .footer-band{height:16px;width:88px;font-size:6px;padding:0 6px}
  .letterhead .footer-contacts{left:94px;right:94px;bottom:6px;font-size:4.8px}

  /* compliments slip */
  .slip{left:460px;top:40px;width:700px;height:320px}
  .slip .brand{left:0;top:32px}
  .slip .brand-lead{width:50px}
  .slip .brand-name{font-size:24px}
  .slip .owner-name{left:86px;top:70px;font-size:14px}
  .slip .member-badge{right:0;top:150px}
  .slip .badge-square{width:30px;height:30px}
  .slip .badge-rule{width:60px;margin-left:10px}
  .slip .footer-band{height:24px;width:170px;font-size:9px;padding:0 10px}
  .slip .footer-contacts{left:180px;right:180px;bottom:8px;font-size:8px}

  /* business card */
  .card{left:460px;top:400px;width:360px;height:206px}
  .card .brand{left:20px;top:22px}
  .card .brand-name{font-size:18px}
  .card .owner-name{right:20px;top:78px;font-size:12px}
  .card .role{position:absolute;right:20px;top:95px;font-size:7px;color:var(--muted)}
  .card .card-rule{position:absolute;left:20px;right:20px;top:110px;height:2px;background:var(--brand-deep)}
  .card .card-rule::after{content:"";position:absolute;right:0;top:-1px;width:60px;height:4px;background:var(--accent-green)}
  .card .contact-list{position:absolute;left:20px;top:122px;list-style:none;font-size:7.5px;line-height:13px}
  .card .contact-list li{display:flex;align-items:center;gap:6px;white-space:nowrap}
  .card .contact-list svg{width:8px;height:8px;fill:var(--brand-blue)}
  .card .member-badge{right:20px;top:140px}
  .card .badge-square{width:24px;height:24px}
  .card .card-base{position:absolute;left:0;right:0;bottom:0;height:8px;background:var(--brand-blue)}
  .card .card-base::after{content:"";position:absolute;right:0;top:0;width:90px;height:8px;background:var(--accent-green)}

  /* envelope */
  .envelope{left:860px;top:400px;width:300px;height:150px;background:#fafafa}
  .envelope svg.flap{position:absolute;left:0;top:0;width:300px;height:150px}
  .envelope .brand{left:50%;top:60px;transform:translateX(-50%)}
  .envelope .brand-name{font-size:12px}
</style>
</head>
<body>
<main class="stage">

  <section class="sheet letterhead" aria-label="Letterhead">
    <div class="brand"><span class="brand-lead"></span><span class="brand-dot"></span><span class="brand-name">Tide 4 Tide Electrical</span></div>
    <div class="owner-name">Darren Kolvetis</div>
    <div class="member-badge" role="img" aria-label="Guild tradespeople member badge"><span class="badge-square"></span><span class="badge-rule"></span></div>
    <footer class="footer">
      <div class="footer-line"></div>
      <div class="footer-contacts">0400 683 541 · t4t@mail.example · tradefind.example/logan</div>
      <div class="footer-band left">ABN: 57804219362</div>
      <div class="footer-band right">Licence Number: 39417</div>
    </footer>
  </section>

  <section class="sheet slip" aria-label="Compliments slip">
    <div class="brand"><span class="brand-lead"></span><span class="brand-dot"></span><span class="brand-name">Tide 4 Tide Electrical</span></div>
    <div class="owner-name">Darren Kolvetis</div>
    <div class="member-badge" role="img" aria-label="Guild tradespeople member badge"><span class="badge-square"></span><span class="badge-rule"></span></div>
    <footer class="footer">
      <div class="footer-line"></div>
      <div class="footer-contacts">0400 683 541 · t4t@mail.example · tradefind.example/logan</div>
      <div class="footer-band left">ABN: 57804219362</div>
      <div class="footer-band right">Licence Number: 39417</div>
    </footer>
  </section>

  <section class="sheet card" aria-label="Business card">
    <div class="brand"><span class="brand-dot"></span><span class="brand-name">Tide 4 Tide Electrical</span></div>
    <div class="owner-name">Darren Kolvetis</div>
    <div class="role">Designation</div>
    <div class="card-rule"></div>
    <ul class="contact-list">
      <li><svg viewBox="0 0 10 10"><path d="M2 1l2 2-1 1.5c.6 1.2 1.3 1.9 2.5 2.5L7 6l2 2-1.5 1.5C4.5 9 1 5.5.5 2.5z"/></svg>0400 683 541</li>
      <li><svg viewBox="0 0 10 10"><path d="M0 2h10v6H0zM0 2l5 3.5L10 2"/></svg>t4t@mail.example</li>
      <li><svg viewBox="0 0 10 10"><circle cx="5" cy="5" r="4.5"/></svg>tradefind.example/logan</li>
      <li><svg viewBox="0 0 10 10"><rect x="1" y="1" width="8" height="8"/></svg>Abn: 57804219362</li>
      <li><svg viewBox="0 0 10 10"><rect x="1" y="1" width="8" height="8"/></svg>Licence Number: 39417</li>
    </ul>
    <div class="member-badge" role="img" aria-label="Guild tradespeople member badge"><span class="badge-square"></span></div>
    <div class="card-base"></div>
  </section>

  <section class="sheet envelope" aria-label="Envelope">
    <svg class="flap" viewBox="0 0 300 150" aria-hidden="true"><path d="M0 0 L150 45 L300 0" fill="none" stroke="#dcdcdf" stroke-width="1"/></svg>
    <div class="brand"><span class="brand-dot"></span><span class="brand-name">Tide 4 Tide Electrical</span></div>
  </section>

</main>
</body>
</html>
```